Dellavon Brokerage LLC product offerings and how to contact for quotes

A marketing email to new and current clients explaining the products the MGA offers and it's exclusive programs. Looking for a modern/sleek design that catches the eye and doesn't become the traditional spam email. Needs to have hyper links to website.
You can use the current website for details of product offerings for insurance: www.dellavon-example.com.
Target Market(s)
Long haul trucking
Industry/Entity Type
Trucking
Colors
0054AA
0677BA
7BADD7
CADEEF
E8F1F8
Requirements
Must have
- Color theme, informative, use of trucking art. Links to website.
Nice to have
- Catchy subject line; want to catch readers eye

```html
<!DOCTYPE html>
<html lang="en">
<head>
<meta charset="utf-8">
<title>Dellavon Brokerage LLC – Our Products</title>
<link rel="stylesheet" href="https://fonts.googleapis.com/css2?family=Open+Sans:wght@400;600;700&family=Poppins:wght@400;500;600&display=swap">
<style>
:root{
  --stage:#8c8c8c;
  --navy:#0547a0;
  --navy-deep:#043a8a;
  --sky:#1a9be0;
  --sky-light:#2ea7e8;
  --title-blue:#0a4aa0;
  --page:#f4f8fd;
  --about-bg:#ebebeb;
  --footer-bg:#eaf6fd;
  --ink:#3b3b3b;
  --ink-dark:#222;
  --white:#fff;
}
*{margin:0;padding:0;box-sizing:border-box}
html,body{width:1200px;height:2414px;overflow:hidden;background:var(--stage)}
.sheet{
  position:absolute;left:202.5px;top:166.9px;width:848px;height:2220px;
  transform:scale(0.9375);transform-origin:0 0;
  background:var(--page);overflow:hidden;
  font-family:"Open Sans",Arial,sans-serif;color:var(--ink);
}
.abs{position:absolute}
/* header */
.topbar{left:0;top:0;width:848px;height:110px;background:var(--white)}
.brand{left:88px;top:38px;display:flex;align-items:center;gap:10px}
.brand-mark{width:22px;height:22px;background:var(--navy)}
.brand-name{font-family:"Open Sans",sans-serif;font-weight:700;font-size:28px;color:var(--navy);letter-spacing:.5px}
.top-phone{left:549px;top:33px;display:flex;align-items:center;gap:10px;text-decoration:none}
.icon-tile{width:36px;height:36px;border-radius:7px;background:linear-gradient(135deg,var(--sky-light),var(--navy));display:flex;align-items:center;justify-content:center}
.top-phone span{font-family:"Poppins",sans-serif;font-weight:600;font-size:22px;color:var(--ink-dark);letter-spacing:.5px}
/* hero */
.hero{left:0;top:110px;width:848px;height:480px}
.hero-title{left:88px;top:170px;width:340px;color:var(--white);font-weight:700;font-size:28.5px;line-height:43px;letter-spacing:.2px}
.hero-btn{left:88px;top:356px;width:178px;height:48px;border-radius:8px;background:var(--sky);color:var(--white);font-weight:600;font-size:15px;display:flex;align-items:center;justify-content:center;text-decoration:none}
/* section heading */
.rule-mark{display:flex;align-items:center;gap:6px}
.rule-mark i{display:block;height:1.5px;background:var(--navy)}
.rule-mark b{display:block;width:10px;height:10px;background:var(--navy);transform:rotate(45deg)}
.section-title{font-weight:700;font-size:30px;color:var(--sky);letter-spacing:.3px}
.products-head{left:0;top:646px;width:848px;display:flex;flex-direction:column;align-items:center;gap:6px}
/* cards */
.card{width:215px;background:var(--white);border-radius:10px;box-shadow:0 2px 10px rgba(20,60,120,.08);padding:19px 20px 0}
.card.raised{box-shadow:0 4px 16px rgba(20,60,120,.16)}
.card-photo{width:175px;height:173px;border-radius:12px}
.card-title{margin-top:20px;text-align:center;font-weight:700;font-size:14px;line-height:21px;color:var(--title-blue)}
.card-text{margin-top:8px;font-size:13.3px;line-height:17.8px;text-align:justify;text-align-last:center;color:var(--ink)}
/* about */
.about{left:0;top:1618px;width:848px;height:602px;background:var(--about-bg)}
.about-head{left:120px;top:1665px}
.about-copy{left:120px;top:1740px;width:330px;font-size:13.8px;line-height:23.4px;text-align:justify;color:var(--ink)}
/* footer */
.contact{text-align:center;font-family:"Poppins",sans-serif;font-size:15.5px;line-height:19px;color:var(--ink-dark);text-decoration:none}
.contact .icon-tile{width:24px;height:24px;border-radius:5px;margin:0 auto 8px}
</style>
</head>
<body>
<main class="sheet">

  <header class="abs topbar"></header>
  <div class="abs brand">
    <span class="brand-mark"></span>
    <span class="brand-name">DELLAVON</span>
  </div>
  <a class="abs top-phone" href="tel:8085550142">
    <span class="icon-tile">
      <svg width="20" height="20" viewBox="0 0 24 24"><path fill="#fff" d="M6.6 10.8a15.1 15.1 0 0 0 6.6 6.6l2.2-2.2a1 1 0 0 1 1-.25 11.4 11.4 0 0 0 3.6.57 1 1 0 0 1 1 1V20a1 1 0 0 1-1 1A17 17 0 0 1 3 4a1 1 0 0 1 1-1h3.5a1 1 0 0 1 1 1c0 1.25.2 2.45.57 3.57a1 1 0 0 1-.25 1z"/></svg>
    </span>
    <span>(808)555-0142</span>
  </a>

  <svg class="abs hero" width="848" height="480" viewBox="0 110 848 480" aria-hidden="false">
    <defs>
      <linearGradient id="truckTones" x1="0" y1="0" x2="1" y2="0">
        <stop offset="0" stop-color="#0547a0"/>
        <stop offset=".18" stop-color="#3a4e8a"/>
        <stop offset=".45" stop-color="#c3233a"/>
        <stop offset=".7" stop-color="#b8283c"/>
        <stop offset="1" stop-color="#d9dde2"/>
      </linearGradient>
      <linearGradient id="skyTones" x1="0" y1="0" x2="0" y2="1">
        <stop offset="0" stop-color="#8a7a3a" stop-opacity=".6"/>
        <stop offset=".4" stop-color="#000" stop-opacity="0"/>
      </linearGradient>
    </defs>
    <polygon points="0,110 848,110 848,445 350,575 0,442" fill="#0547a0"/>
    <g role="img" aria-label="Red semi truck with white trailer on an autumn highway">
      <polygon points="380,110 848,110 848,445 420,556 380,540" fill="url(#truckTones)"/>
      <polygon points="380,110 848,110 848,300 380,300" fill="url(#skyTones)"/>
    </g>
    <polyline points="0,442 350,574 848,445" fill="none" stroke="#1a9be0" stroke-width="3"/>
    <polyline points="0,446 350,584 848,452" fill="none" stroke="#043a8a" stroke-width="3"/>
  </svg>
  <h1 class="abs hero-title">SPECIALIZING IN TOUGH-TO-PLACE RISKS WITH UNMATCHED CUSTOMER SERVICE</h1>
  <a class="abs hero-btn" href="https://www.dellavon-example.com">VIEW OUR SITE</a>

  <div class="abs products-head">
    <div class="rule-mark"><i style="width:32px"></i><b></b><i style="width:32px"></i></div>
    <h2 class="section-title">OUR PRODUCTS</h2>
  </div>

  <article class="abs card" style="left:86px;top:743px;height:390px">
    <div class="card-photo" role="img" aria-label="White semi trucks parked at a loading dock" style="background:linear-gradient(180deg,#a9b8c9,#e3e6ea 55%,#8d939b)"></div>
    <h3 class="card-title">AUTO LIABILITY</h3>
    <p class="card-text">Liability insurance is a part of the general insurance system of risk financing to protect the purchaser (the "insured") from the risks of liabilities imposed by lawsuits and similar claims.</p>
  </article>
  <article class="abs card" style="left:318px;top:743px;height:390px">
    <div class="card-photo" role="img" aria-label="Close view of a tanker truck on the road" style="background:linear-gradient(135deg,#3c3f44,#d7d9dc 50%,#6d6f73)"></div>
    <h3 class="card-title">AUTO PHYSICAL DAMAGE</h3>
    <p class="card-text">Physical Damage insurance is a type of insurance that covers damages to your truck and trailer. This type of coverage is typically offered as part of an auto insurance policy.</p>
  </article>
  <article class="abs card" style="left:549px;top:743px;height:390px">
    <div class="card-photo" role="img" aria-label="Two trucks driving on a highway through green hills" style="background:linear-gradient(180deg,#a8c6e6,#6f8d5e 45%,#9a9ea3)"></div>
    <h3 class="card-title">GENERAL LIABILITY</h3>
    <p class="card-text">Liability insurance is a part of the general insurance system of risk financing to protect the purchaser (the "insured") from the risks of liabilities imposed by lawsuits and similar claims.</p>
  </article>

  <article class="abs card" style="left:86px;top:1172px;height:405px">
    <div class="card-photo" role="img" aria-label="Two truck drivers reviewing paperwork beside a rig" style="background:linear-gradient(135deg,#c9c2b6,#8a6a52 45%,#b9cc5a 75%,#5a6068)"></div>
    <h3 class="card-title">NON-TRUCKING LIABILITY</h3>
    <p class="card-text">Non-Trucking Liability (NTL) provides coverage in case you cause an accident while you are using your vehicle for non-business or personal use other than transporting goods or merchandise.</p>
  </article>
  <article class="abs card raised" style="left:318px;top:1172px;height:405px">
    <div class="card-photo" role="img" aria-label="Box truck backed up to a warehouse loading bay" style="background:linear-gradient(135deg,#4a4038,#d9d4cc 55%,#5b534b)"></div>
    <h3 class="card-title">MOTOR TRUCK CARGO</h3>
    <p class="card-text">Provides liability insurance for truckers who carry the cargo of others and is used in the event that the cargo is destroyed, damaged, stolen, or otherwise declared a loss while in the process.</p>
  </article>
  <article class="abs card" style="left:549px;top:1172px;height:405px">
    <div class="card-photo" role="img" aria-label="Row of parked semi trucks under a blue sky" style="background:linear-gradient(180deg,#5f9ad6,#c8d6e4 50%,#7b7f84)"></div>
    <h3 class="card-title">UMBRELLA &amp; EXCESS<br>COVERAGE</h3>
    <p class="card-text">Most Umbrella and Excess Liability policies are not written on standardized forms, so it is always important to read your policies to see what they actually cover.</p>
  </article>

  <section class="abs about"></section>
  <div class="abs about-head">
    <div class="rule-mark"><b></b><i style="width:34px"></i></div>
    <h2 class="section-title" style="margin-top:6px">ABOUT US</h2>
  </div>
  <p class="abs about-copy">Dellavon Brokerage LLC is a boutique Managing General Agent (MGA) specializing in commercial insurance for truckers. It was formed with one goal in mind: to help small independent trucking retailers with tough to place risks while giving them exceptional customer service experience. With knowledge and expertise in every aspect of a typical trucking operation, we want to be the preferred choice for our clients. We will never be too busy to respond back to your e-mails or phone calls.</p>

  <svg class="abs" style="left:490px;top:1694px" width="226" height="256" viewBox="490 1694 226 256">
    <defs>
      <linearGradient id="forestTones" x1="0" y1="0" x2="0" y2="1">
        <stop offset="0" stop-color="#cfe0ee"/>
        <stop offset=".25" stop-color="#4f7a3c"/>
        <stop offset=".6" stop-color="#d6d9dc"/>
        <stop offset="1" stop-color="#7d8186"/>
      </linearGradient>
    </defs>
    <polygon role="img" aria-label="White semi truck on a road lined with forest" points="603,1699 710,1761 710,1883 603,1945 496,1883 496,1761" fill="url(#forestTones)" stroke="#0547a0" stroke-width="3"/>
  </svg>

  <svg class="abs" style="left:0;top:2020px" width="848" height="200" viewBox="0 2020 848 200">
    <polygon points="0,2092 416,2030 848,2092 848,2220 0,2220" fill="#eaf6fd"/>
    <polyline points="0,2090 416,2027 848,2090" fill="none" stroke="#043a8a" stroke-width="4"/>
    <polyline points="0,2095 416,2034 848,2095" fill="none" stroke="#1a9be0" stroke-width="3"/>
  </svg>

  <a class="abs contact" style="left:78px;top:2116px;width:140px" href="tel:8085550142">
    <span class="icon-tile"><svg width="15" height="15" viewBox="0 0 24 24"><path fill="#fff" d="M6.6 10.8a15.1 15.1 0 0 0 6.6 6.6l2.2-2.2a1 1 0 0 1 1-.25 11.4 11.4 0 0 0 3.6.57 1 1 0 0 1 1 1V20a1 1 0 0 1-1 1A17 17 0 0 1 3 4a1 1 0 0 1 1-1h3.5a1 1 0 0 1 1 1c0 1.25.2 2.45.57 3.57a1 1 0 0 1-.25 1z"/></svg></span>
    (808)555-0142
  </a>
  <div class="abs contact" style="left:300px;top:2111px;width:230px">
    <span class="icon-tile"><svg width="14" height="16" viewBox="0 0 24 24"><path fill="#fff" d="M12 2a7 7 0 0 0-7 7c0 5.2 7 13 7 13s7-7.8 7-13a7 7 0 0 0-7-7zm0 9.5A2.5 2.5 0 1 1 12 6.5a2.5 2.5 0 0 1 0 5z"/></svg></span>
    1200 Harbor View Ave Ste<br>300 Honolulu, HI 96801
  </div>
  <a class="abs contact" style="left:590px;top:2110px;width:205px" href="https://www.dellavon-example.com">
    <span class="icon-tile"><svg width="16" height="16" viewBox="0 0 24 24" fill="none" stroke="#fff" stroke-width="1.6"><circle cx="12" cy="12" r="9"/><ellipse cx="12" cy="12" rx="4" ry="9"/><path d="M3 12h18M5 7h14M5 17h14"/></svg></span>
    www.dellavon-example.com
  </a>

</main>
</body>
</html>
```